Flyer design needed for services offered and to show reviews from previous customers

I would like a Flyer designed showing some of the services i offer:
-LED lighting upgrades (pot lights, accent & commercial)
-Electrical repairs & Service work
- Fayglowen lighting
- TV wall mounts
My website is Voltarisa.ca if you need any photos from there in higher quality please let me know and i can provide them.

I want it to have a couple reviews from previous customers (attached links to facebook and google page)
Google:
https://revpage.example/r/QZ8kd4mtpWhaJXo/review
Facebook:
https://www.socialbook.example/Voltarisa-Contracting-Ltd-552918730461283

```html
<!DOCTYPE html>
<html lang="en">
<head>
<meta charset="utf-8">
<title>Voltarisa Contracting Ltd – Services Flyer</title>
<link href="https://fonts.googleapis.com/css2?family=Red+Hat+Display:wght@400;500;700;900&display=swap" rel="stylesheet">
<style>
  :root {
    --canvas: #e8e6e3;
    --gray-dark: #4a4b4d;
    --gray-mid: #5e5f62;
    --gray-light: #7a7b7e;
    --orange: #f07a1a;
    --white: #ffffff;
    --ink: #1f1f1f;
    --rule: #c9c9c9;
  }
  * { box-sizing: border-box; margin: 0; padding: 0; }
  html, body { width: 1200px; height: 1200px; overflow: hidden; }
  body {
    background: var(--canvas);
    font-family: "Red Hat Display", Arial, sans-serif;
    color: var(--ink);
    position: relative;
  }
  .flyer {
    position: absolute;
    left: 200px; top: 37px;
    width: 800px; height: 1126px;
    background: var(--white);
    overflow: hidden;
  }
  .flyer-header { position: absolute; left: 0; top: 0; width: 800px; height: 560px; }
  .brand-badge {
    position: absolute; left: 28px; top: 158px;
    width: 174px; height: 174px; border-radius: 50%;
    background: var(--white);
    border: 6px solid var(--ink);
    display: flex; align-items: center; justify-content: center;
    text-align: center;
    padding: 0 18px;
  }
  .brand-name {
    font-weight: 900; font-size: 16px; line-height: 1.2;
    color: var(--ink); letter-spacing: 0.5px; text-transform: uppercase;
  }
  .intro {
    position: absolute; left: 65px; top: 348px; width: 670px;
    color: var(--white); font-size: 15px; line-height: 1.4;
    text-align: center; font-weight: 400;
  }
  .services {
    position: absolute; left: 48px; top: 483px; width: 705px; height: 230px;
    background: var(--white); border: 3px solid var(--gray-dark);
    border-radius: 16px;
  }
  .services-rule {
    position: absolute; top: 30px; height: 2px; width: 115px; background: var(--rule);
  }
  .services-rule.left { left: 28px; }
  .services-rule.right { right: 28px; }
  .services-tab {
    position: absolute; left: 163px; top: -3px; width: 372px; height: 60px;
  }
  .services-title {
    position: absolute; left: 163px; top: -3px; width: 372px; height: 56px;
    display: flex; align-items: center; justify-content: center;
    color: var(--white); font-weight: 900; font-size: 40px; letter-spacing: 0.5px;
  }
  .service {
    position: absolute; display: flex; align-items: center; gap: 18px;
  }
  .service-icon {
    width: 52px; height: 52px; border-radius: 50%;
    background: var(--gray-dark); border: 3px solid var(--orange);
    display: flex; align-items: center; justify-content: center; flex: none;
  }
  .service-name { font-weight: 700; font-size: 20px; line-height: 1.1; }
  .service-note { display: block; font-weight: 500; font-size: 11.5px; margin-top: 1px; }
  .service.s1 { left: 23px; top: 79px; }
  .service.s2 { left: 23px; top: 154px; }
  .service.s3 { left: 435px; top: 79px; }
  .service.s4 { left: 435px; top: 157px; }
  .reviews-bar {
    position: absolute; left: 48px; top: 730px; width: 705px; height: 48px;
    background: linear-gradient(180deg, var(--gray-light), var(--gray-dark));
    border-radius: 8px;
    color: var(--white); font-weight: 900; font-size: 27px; letter-spacing: 0.5px;
    display: flex; align-items: center; justify-content: center;
  }
  .review {
    position: absolute; top: 798px; text-align: center;
    font-size: 13.6px; line-height: 1.28;
  }
  .review.r1 { left: 48px; width: 216px; }
  .review.r2 { left: 284px; width: 204px; }
  .review.r3 { left: 516px; width: 226px; }
  .stars { color: var(--orange); font-size: 25px; letter-spacing: 2px; line-height: 1; margin-bottom: 10px; }
  .review-author { font-weight: 700; font-size: 15px; margin-top: 12px; }
  .review-divider {
    position: absolute; top: 800px; height: 198px;
    border-left: 2px dashed var(--rule);
  }
  .review-divider.d1 { left: 275px; }
  .review-divider.d2 { left: 503px; }
  .footer-base {
    position: absolute; left: 0; top: 1080px; width: 800px; height: 46px; background: var(--gray-mid);
  }
  .footer-band { position: absolute; left: 52px; top: 1034px; width: 700px; height: 92px; }
  .contacts {
    position: absolute; left: 52px; top: 1034px; width: 700px; height: 92px;
    display: flex; align-items: center; justify-content: center;
    color: var(--white); font-weight: 700; font-size: 17px;
  }
  .contact { display: flex; align-items: center; gap: 8px; padding: 0 22px; }
  .contact + .contact { border-left: 2px solid rgba(255,255,255,0.85); }
</style>
</head>
<body>
<main class="flyer">

  <svg class="flyer-header" viewBox="0 0 800 560">
    <defs>
      <linearGradient id="headerGray" x1="0" y1="0" x2="0" y2="1">
        <stop offset="0" stop-color="#6a6b6e"/>
        <stop offset="1" stop-color="#4a4b4d"/>
      </linearGradient>
      <linearGradient id="kitchenTone" x1="0" y1="0" x2="1" y2="1">
        <stop offset="0" stop-color="#e6e3de"/>
        <stop offset="0.6" stop-color="#bdbab5"/>
        <stop offset="1" stop-color="#7d7c79"/>
      </linearGradient>
      <linearGradient id="stairsTone" x1="0" y1="0" x2="1" y2="1">
        <stop offset="0" stop-color="#4b5157"/>
        <stop offset="0.55" stop-color="#262829"/>
        <stop offset="1" stop-color="#6b5530"/>
      </linearGradient>
      <linearGradient id="bandOrange" x1="0" y1="0" x2="1" y2="0">
        <stop offset="0" stop-color="#f58a24"/>
        <stop offset="1" stop-color="#e0600c"/>
      </linearGradient>
    </defs>
    <rect width="800" height="560" fill="url(#headerGray)"/>
    <g role="img" aria-label="Photo of a modern kitchen with white cabinets and under-cabinet lighting">
      <path d="M0 0 H520 L330 285 Q180 250 0 282 Z" fill="url(#kitchenTone)"/>
    </g>
    <path d="M520 0 H575 L380 292 Q355 290 330 285 Z" fill="#3d3e40"/>
    <g role="img" aria-label="Photo of dark stairs lit by warm step lights">
      <path d="M575 0 H800 V215 L560 318 Q450 350 395 292 Z" fill="url(#stairsTone)"/>
    </g>
    <path d="M388 296 Q450 362 562 330 L800 228 V262 L570 352 Q440 392 378 300 Z" fill="url(#bandOrange)"/>
  </svg>

  <div class="brand-badge">
    <span class="brand-name">Voltarisa<br>Contracting<br>Ltd</span>
  </div>

  <p class="intro">Whether you need some new lighting installed or need your entire panel replaced, we are here to help! Our goal is to provide you with the best possible service. This means the work is done correctly the first time, there is no mess left behind when it’s completed, and your satisfaction is guaranteed. We provide service in Residential, Commercial and Industrial Electrical Systems. Feel free to give us a call, text or email and we will gladly get in touch to schedule a service call or free quote!</p>

  <section class="services">
    <span class="services-rule left"></span>
    <span class="services-rule right"></span>
    <svg class="services-tab" viewBox="0 0 372 60">
      <defs>
        <linearGradient id="tabOrange" x1="0" y1="0" x2="0" y2="1">
          <stop offset="0" stop-color="#f58a24"/>
          <stop offset="1" stop-color="#e0600c"/>
        </linearGradient>
      </defs>
      <path d="M0 0 H372 L350 48 Q345 58 333 58 H39 Q27 58 22 48 Z" fill="url(#tabOrange)"/>
    </svg>
    <h2 class="services-title">SERVICES</h2>

    <div class="service s1">
      <span class="service-icon">
        <svg width="28" height="28" viewBox="0 0 24 24" fill="none" stroke="#fff" stroke-width="1.6" stroke-linecap="round">
          <path d="M9 17h6M10 20h4M12 4a5 5 0 0 0-3 9v3h6v-3a5 5 0 0 0-3-9z"/>
          <path d="M12 1v1M4 5l1 1M20 5l-1 1M1 11h1M22 11h1"/>
        </svg>
      </span>
      <span class="service-name">LED lighting upgrades<span class="service-note">(pot lights, accent &amp; commercial)</span></span>
    </div>
    <div class="service s2">
      <span class="service-icon">
        <svg width="28" height="28" viewBox="0 0 24 24" fill="none" stroke="#fff" stroke-width="1.6" stroke-linejoin="round">
          <circle cx="12" cy="12" r="8"/>
          <path d="M13 6l-4 7h3l-1 5 4-7h-3z"/>
        </svg>
      </span>
      <span class="service-name">Electrical repairs &amp; Service work</span>
    </div>
    <div class="service s3">
      <span class="service-icon">
        <svg width="28" height="28" viewBox="0 0 24 24" fill="none" stroke="#fff" stroke-width="1.6" stroke-linejoin="round">
          <path d="M3 11l9-7 9 7M5 10v10h14V10"/>
          <path d="M12 12v4"/>
        </svg>
      </span>
      <span class="service-name">Fayglowen lighting</span>
    </div>
    <div class="service s4">
      <span class="service-icon">
        <svg width="28" height="28" viewBox="0 0 24 24" fill="none" stroke="#fff" stroke-width="1.6">
          <rect x="5" y="6" width="14" height="10" rx="1"/>
          <path d="M3 4v14M21 4v14M9 20h6"/>
        </svg>
      </span>
      <span class="service-name">TV wall mounts</span>
    </div>
  </section>

  <h2 class="reviews-bar">REVIEWS</h2>

  <article class="review r1">
    <div class="stars">★★★★★</div>
    <p>“Dorian did some shop work for me and did a great job. Hooked up a couple of hoists and compressor in an old shop that had several renovations. He figured it out. Was very professional, punctual and fair. I would recommend him and will use him again.”</p>
    <p class="review-author">Merrick Halvorsen</p>
  </article>
  <span class="review-divider d1"></span>
  <article class="review r2">
    <div class="stars">★★★★★</div>
    <p>“over all a very positive experience will definitely recommended and wont hesitate to use them again.”</p>
    <p class="review-author">Lena Marchetti</p>
  </article>
  <span class="review-divider d2"></span>
  <article class="review r3">
    <div class="stars">★★★★★</div>
    <p>“We had Dorian install the electricalfor our garage. He was professional, on time and coordinated with our garage contractor to make sure everything was done in sequence. When the inspector came, it was a one and done. When we do our basement renovation, we will definitely be calling Dorian back.”</p>
    <p class="review-author">Lena Marchetti</p>
  </article>

  <div class="footer-base"></div>
  <svg class="footer-band" viewBox="0 0 700 92">
    <defs>
      <linearGradient id="footOrange" x1="0" y1="0" x2="1" y2="0">
        <stop offset="0" stop-color="#f07a1a"/>
        <stop offset="1" stop-color="#e8680f"/>
      </linearGradient>
    </defs>
    <path d="M40 0 H680 Q700 0 696 18 L680 92 H0 L22 14 Q26 0 40 0 Z" fill="url(#footOrange)"/>
  </svg>
  <div class="contacts">
    <span class="contact">
      <svg width="16" height="16" viewBox="0 0 24 24"><circle cx="12" cy="12" r="11" fill="#fff"/><path d="M8 6l2 3-1 1.5a8 8 0 0 0 4.5 4.5L15 14l3 2-1 2.5c-5 0-10-5-10-10z" fill="#f07a1a"/></svg>
      (555) 218-6093
    </span>
    <span class="contact">
      <svg width="18" height="14" viewBox="0 0 24 18" fill="none" stroke="#fff" stroke-width="1.8"><rect x="1" y="1" width="22" height="16" rx="1.5"/><path d="M1 2l11 8 11-8"/></svg>
      Dorian@Voltarisa.ca
    </span>
    <span class="contact">
      <svg width="16" height="16" viewBox="0 0 24 24" fill="none" stroke="#fff" stroke-width="1.8"><circle cx="12" cy="12" r="10"/><path d="M2 12h20M12 2c3 3 3 17 0 20M12 2c-3 3-3 17 0 20"/></svg>
      www.voltarisa.ca
    </span>
  </div>

</main>
</body>
</html>
```